larkwind flakies snack packaging

We are a new startup snack company that need a design for a snack packaging. Our snack goes by the name of larkwind flakies. Its a traditional snack usually eaten during festive seasons in south east asia region. The idea is to revolutionize the notion of the snack from one that is eaten during these celebratory seasons to an everyday one. The packaging design should be modern and minimalist yet fun too, also taking into consideration that it should not appear to be too childish. It should stand out from the other snacks products like potato chips etc if placed on the same shelf. The colour scheme is not decided yet as we are open to more ideas but colours should be complementary and not more than 2 or 3 hopefully. There should be also be an enthic sense of south east asian features on the design and it should reflects the Chinese, Malay and indian heritage. It need not be too obvious, a subtle kind should suffice. The packaging should also have the particular graphic/shape of the mould that i have upload followed by the picture of the snack. I have included a mock up of the logo of my company. Proposed designs can feel free to alter the larkwind graphic to a more modern, minimalist yet whimsical and fun. Proposed designs should have a front and back view of the packaging. We are looking to launch at 4 to 5 flavours like white sesame, black sesame, peanuts with white sesame and original.
Updates

Project Deadline Extended
Reason: Not enough submissions coming in yet.

Project Deadline Extended
Reason: Extension of deadline to allow more designs to come in.

Target Market(s)

All ages from as young as 5 to 6 years old to 60 to 70s.

Industry/Entity Type

It Company

Font styles to use
Other font styles liked:
• Fonts should be simple and minimalist. Easy for elderly to read without straining the eyes.

Requirements
Must have
• My logo which I have designed. Designers can feel free to tweak and enhance the design of the logo. The colour is not definite yet. Consumers must know what
• we are selling from the design of the packaging without guessing how it look
• like. The suggested packaging dimension is 17cm (W) by 23.5cm (H).
Nice to have
• We are looking to print the package using kraft paper which I have attached.
Should not have
• religious inclination of motifs, logo etc.

```html
<!DOCTYPE html>
<html lang="en">
<head>
<meta charset="utf-8">
<title>larkwind flakies – snack pouch range</title>
<link rel="stylesheet" href="https://fonts.googleapis.com/css2?family=Josefin+Sans:wght@300;400&family=Quicksand:wght@500&display=swap">
<style>
  :root {
    --backdrop: #e6e5e5;
    --kraft-light: #d2a878;
    --kraft: #c4976a;
    --kraft-dark: #b3845a;
    --red: #b4181f;
    --black: #1e1b1b;
    --orange: #e2431f;
    --cream: #f7efe7;
    --ink: #2a1d14;
  }
  * { box-sizing: border-box; margin: 0; padding: 0; }
  html, body { width: 1176px; height: 1200px; overflow: hidden; }
  body { background: var(--backdrop); position: relative; }

  .pouch {
    --accent: var(--red);
    --flavour-ink: var(--red);
    position: absolute;
    width: 338px;
    height: 520px;
    border-radius: 4px;
    background: linear-gradient(165deg, var(--kraft-light) 0%, var(--kraft) 45%, var(--kraft-dark) 100%);
    overflow: hidden;
  }
  .pouch--top { left: 419px; top: 50px; --flavour-ink: var(--black); }
  .pouch--original { left: 55px; top: 640px; }
  .pouch--black { left: 419px; top: 640px; --accent: var(--black); --flavour-ink: var(--black); }
  .pouch--white { left: 783px; top: 640px; --accent: var(--orange); --flavour-ink: var(--orange); }

  .pouch__top-band { position: absolute; left: 0; top: 0; width: 100%; height: 10px; background: var(--accent); }
  .pouch__banner { position: absolute; left: 81px; top: 0; width: 176px; height: 232px; }
  .pouch__banner path { fill: var(--accent); }

  .brand { position: absolute; left: 81px; width: 176px; top: 0; height: 220px; text-align: center; color: var(--cream); font-family: "Quicksand", sans-serif; }
  .brand__mark { position: absolute; left: 53px; top: 58px; width: 70px; height: 70px; border: 5px solid var(--cream); border-radius: 50%; }
  .brand__name { position: absolute; left: 0; width: 100%; top: 156px; font-size: 20px; font-weight: 500; letter-spacing: 0.2px; line-height: 1; white-space: nowrap; }

  .flavour { position: absolute; left: 0; width: 100%; top: 268px; text-align: center; font-family: "Josefin Sans", sans-serif; font-weight: 300; font-size: 31px; letter-spacing: 0.5px; color: var(--flavour-ink); white-space: nowrap; }
  .net-weight { position: absolute; left: 0; width: 100%; top: 420px; text-align: center; font-family: "Quicksand", sans-serif; font-weight: 500; font-size: 12.5px; color: var(--ink); }

  .pouch__pattern { position: absolute; left: 14px; right: 14px; top: 446px; height: 38px; background: linear-gradient(90deg, rgba(0,0,0,0.12), rgba(0,0,0,0.2), rgba(0,0,0,0.12)); border-radius: 3px; }
  .pouch--white .pouch__pattern, .pouch--original .pouch__pattern { background: linear-gradient(90deg, rgba(180,24,31,0.18), rgba(180,24,31,0.3), rgba(180,24,31,0.18)); }
  .pouch__bottom-band { position: absolute; left: 0; bottom: 0; width: 100%; height: 22px; background: var(--accent); }
</style>
</head>
<body>

<section class="pouch pouch--top" aria-label="Sesame black pouch, red edition">
  <div class="pouch__top-band"></div>
  <svg class="pouch__banner" viewBox="0 0 176 232" aria-hidden="true"><path d="M0 0H176V212Q88 240 0 212Z"/></svg>
  <div class="brand">
    <div class="brand__mark"></div>
    <div class="brand__name">larkwind flakies</div>
  </div>
  <div class="flavour">SESAME BLACK</div>
  <div class="net-weight">Net Weight. 70 gram</div>
  <div class="pouch__pattern" role="img" aria-label="Band of ornamental mould-shape pattern"></div>
  <div class="pouch__bottom-band"></div>
</section>

<section class="pouch pouch--original" aria-label="Original flavour pouch">
  <div class="pouch__top-band"></div>
  <svg class="pouch__banner" viewBox="0 0 176 232" aria-hidden="true"><path d="M0 0H176V212Q88 240 0 212Z"/></svg>
  <div class="brand">
    <div class="brand__mark"></div>
    <div class="brand__name">larkwind flakies</div>
  </div>
  <div class="flavour">ORIGINAL</div>
  <div class="net-weight">Net Weight. 70 gram</div>
  <div class="pouch__pattern" role="img" aria-label="Band of ornamental mould-shape pattern"></div>
  <div class="pouch__bottom-band"></div>
</section>

<section class="pouch pouch--black" aria-label="Sesame black flavour pouch">
  <div class="pouch__top-band"></div>
  <svg class="pouch__banner" viewBox="0 0 176 232" aria-hidden="true"><path d="M0 0H176V212Q88 240 0 212Z"/></svg>
  <div class="brand">
    <div class="brand__mark"></div>
    <div class="brand__name">larkwind flakies</div>
  </div>
  <div class="flavour">SESAME BLACK</div>
  <div class="net-weight">Net Weight. 70 gram</div>
  <div class="pouch__pattern" role="img" aria-label="Band of ornamental mould-shape pattern"></div>
  <div class="pouch__bottom-band"></div>
</section>

<section class="pouch pouch--white" aria-label="White sesame flavour pouch">
  <div class="pouch__top-band"></div>
  <svg class="pouch__banner" viewBox="0 0 176 232" aria-hidden="true"><path d="M0 0H176V212Q88 240 0 212Z"/></svg>
  <div class="brand">
    <div class="brand__mark"></div>
    <div class="brand__name">larkwind flakies</div>
  </div>
  <div class="flavour">WHITE SESAME</div>
  <div class="net-weight">Net Weight. 70 gram</div>
  <div class="pouch__pattern" role="img" aria-label="Band of ornamental mould-shape pattern"></div>
  <div class="pouch__bottom-band"></div>
</section>

</body>
</html>
```